Business card design for a world class martial arts and group fitness facility

We need a professional and eye catching design for a business card. The card will be used in networking as well as marketing.
We are a martial arts facility offering Taekwondo, Brazilian Jiu Jitsu, and group fitness. All of our programs are geared for kids and adults.
Our Taekwondo program is lead by a Hall of Fame instructor who was Instructor of the Year in 2015.
Our Brazilian Jiu Jitsu program is lead by a wold class instructor who is also a part of the renown Brazilian KLO team.
We offer 3 focused group fitness programs: Ridge kickboxing, Tandem Fitness, and The Quarry which are all lead by certified instructors in a small group setting.
Our facility is state of the art and has been recognized as such in nationally published magazines.
Our business is named The Forge which is the linear logo that is attached. This is the main logo. I also attached a circular logo we have used in some marketing material. Our Jiu Jitsu program is the KLO team logo. The Taekwondo program is the VORTEN Prime. It would be nice to somehow incorporate all 3 logos, but The Forge is most important.
We would like to use all 3 logos if possible but The Forge is the most important. We would like to have a place for a staff member's name while keeping the focus on the programs we offer.

```html
<!DOCTYPE html>
<html lang="en">
<head>
<meta charset="utf-8">
<title>The Forge – Business Card</title>
<link href="https://fonts.googleapis.com/css2?family=Lato:wght@300;400;700;900&display=swap" rel="stylesheet">
<style>
  :root {
    --canvas: #e9e6e2;
    --card-dark: #2a2a2c;
    --card-dark-2: #3a3a3d;
    --brand-red: #d8132a;
    --brand-red-light: #e8394c;
    --paper: #ffffff;
    --ink-grey: #6e6e70;
    --text-light: #ffffff;
  }
  html, body {
    margin: 0;
    padding: 0;
    width: 1200px;
    height: 913px;
    overflow: hidden;
    background: var(--canvas);
    font-family: "Lato", sans-serif;
  }
  .canvas {
    position: relative;
    width: 1200px;
    height: 913px;
  }
  .card {
    position: absolute;
    width: 640px;
    height: 366px;
    box-shadow: 0 10px 28px rgba(0,0,0,0.25);
  }
  .card svg { display: block; }
  .card--logos { left: 60px; top: 70px; }
  .card--contact { left: 500px; top: 477px; }
  .wordmark { font-family: "Lato", sans-serif; font-weight: 900; }
  .staff-name { font-family: "Lato", sans-serif; font-size: 26px; fill: var(--text-light); letter-spacing: 1px; }
  .staff-name .first { font-weight: 900; }
  .staff-name .last { font-weight: 300; }
  .staff-title { font-family: "Lato", sans-serif; font-weight: 400; font-size: 15px; fill: var(--text-light); }
  .contact-line { font-family: "Lato", sans-serif; font-weight: 400; font-size: 14px; fill: var(--text-light); letter-spacing: 0.3px; }
</style>
</head>
<body>
<main class="canvas">

  <!-- Logo side -->
  <section class="card card--logos" aria-label="Card front with program names">
    <svg width="640" height="366" viewBox="0 0 640 366" xmlns="http://www.w3.org/2000/svg">
      <defs>
        <linearGradient id="darkFace" x1="0" y1="0" x2="1" y2="1">
          <stop offset="0" stop-color="var(--card-dark-2)"/>
          <stop offset="1" stop-color="var(--card-dark)"/>
        </linearGradient>
        <linearGradient id="redPanel" x1="0" y1="0" x2="1" y2="1">
          <stop offset="0" stop-color="var(--brand-red-light)"/>
          <stop offset="1" stop-color="var(--brand-red)"/>
        </linearGradient>
      </defs>
      <rect class="card-face" width="640" height="366" fill="url(#darkFace)"/>
      <rect class="logo-band" x="0" y="132" width="640" height="118" fill="var(--paper)"/>
      <polygon class="feature-panel" points="214,262 246,120 450,120 418,262" fill="url(#redPanel)"/>

      <g class="program-mark program-mark--klo">
        <circle cx="108" cy="191" r="46" fill="var(--card-dark)" stroke="var(--brand-red)" stroke-width="4"/>
        <text class="wordmark" x="108" y="201" text-anchor="middle" font-size="28" fill="var(--text-light)">KLO</text>
      </g>

      <text class="wordmark" x="332" y="202" text-anchor="middle" font-size="36" fill="var(--text-light)">The Forge</text>

      <text class="wordmark" x="546" y="199" text-anchor="middle" font-size="22" fill="var(--card-dark)">VORTEN Prime</text>
    </svg>
  </section>

  <!-- Contact side -->
  <section class="card card--contact" aria-label="Card back with staff contact details">
    <svg width="640" height="366" viewBox="0 0 640 366" xmlns="http://www.w3.org/2000/svg">
      <rect class="card-face" width="640" height="366" fill="var(--paper)"/>

      <g class="main-mark">
        <circle cx="470" cy="90" r="54" fill="none" stroke="var(--ink-grey)" stroke-width="4"/>
        <text class="wordmark" x="470" y="98" text-anchor="middle" font-size="24" fill="var(--ink-grey)">The Forge</text>
      </g>

      <polygon class="contact-band" points="0,250 540,250 640,190 640,366 0,366" fill="var(--card-dark)"/>
      <rect class="accent-frame" x="528" y="150" width="130" height="84" rx="16" fill="var(--card-dark-2)" stroke="var(--brand-red)" stroke-width="6"/>

      <polygon class="name-band" points="0,132 310,132 280,208 0,208" fill="var(--brand-red)"/>
      <text class="staff-name" x="30" y="168"><tspan class="first">REID</tspan> <tspan class="last">CALLOWAY</tspan></text>
      <text class="staff-title" x="30" y="192">Creative Director</text>

      <text class="contact-line" x="30" y="282">18 Harlow Street Dayton OH 45402</text>

      <g class="contact-item">
        <rect x="30" y="299" width="18" height="18" rx="4" fill="var(--brand-red)"/>
        <path d="M35 303 q-1 4 3 8 q4 4 8 3 l0-2 -3-1 -1 1 q-3-1-5-5 l1-1 -1-3z" fill="var(--text-light)"/>
        <text class="contact-line" x="56" y="313">000 . 4417 . 2290</text>
      </g>
      <g class="contact-item">
        <rect x="30" y="327" width="18" height="18" rx="4" fill="var(--brand-red)"/>
        <rect x="34" y="333" width="10" height="7" fill="var(--text-light)"/>
        <rect x="36" y="330" width="6" height="3" fill="var(--text-light)"/>
        <text class="contact-line" x="56" y="341">000 . 4417 . 2291</text>
      </g>
      <g class="contact-item">
        <rect x="300" y="299" width="18" height="18" rx="4" fill="var(--brand-red)"/>
        <rect x="303" y="304" width="12" height="8" fill="none" stroke="var(--text-light)" stroke-width="1.5"/>
        <path d="M303 304 l6 4 6-4" fill="none" stroke="var(--text-light)" stroke-width="1.5"/>
        <text class="contact-line" x="326" y="313">hello@theforgegym.com</text>
      </g>
      <g class="contact-item">
        <rect x="300" y="327" width="18" height="18" rx="4" fill="var(--brand-red)"/>
        <circle cx="309" cy="336" r="5.5" fill="none" stroke="var(--text-light)" stroke-width="1.5"/>
        <path d="M303.5 336 h11 M309 330.5 v11" stroke="var(--text-light)" stroke-width="1.2"/>
        <text class="contact-line" x="326" y="341">www.theforgegym.com</text>
      </g>
    </svg>
  </section>

</main>
</body>
</html>
```